New Body Mist 250 ml exclusive

We are excited to embark on a new project to design the packaging for body mist:
Lunar Bramble

We are looking for a design that is truly unique and stands out, with a touch of individuality that sets it apart. The design should be eye-catching and visually appealing, drawing attention even from a distance. We want the body mists to have a fun and attractive look that appeals to customers.

To help bring your design to life, we will provide the dimensions of the bottle, which has a capacity of 250ml. The bottle measures 13.3 cm in height and 4.9 cm in diameter (excluding the pump). Additionally, we will also provide the dimensions of the label, which measures 15.1 cm in height and 12.8 cm in width.

We believe that giving you the freedom to put your own unique touch and color choices will help create a truly standout design. We look forward to seeing your creative vision for our body mist.

We shared with you the logo of the body mist and some examples of models that we liked.

Please be informed that the project only includes one design and the remaining three will be completed and paid for through a 1on1 project with the winner of the contest.

Target Market(s)

Supermarket and perfumery stores

Industry/Entity Type

Cosmetics

Font styles to use
Serif

Requirements
Must have
• Uniqueness and attractiveness

```html
<!DOCTYPE html>
<html lang="en">
<head>
<meta charset="utf-8">
<title>Lunar Bramble – Coral Drift Body Mist Label</title>
<link rel="stylesheet" href="https://fonts.googleapis.com/css2?family=Cormorant+Garamond:wght@400;500;600&family=Playfair+Display:wght@400&display=swap">
<style>
  :root {
    --page: #ffffff;
    --teal: #35c4d6;
    --aqua: #6fd8e0;
    --ocean: #1b8fd8;
    --deep: #1167c4;
    --mint: #c8e8b0;
    --white: #ffffff;
    --orchid-light: #efe6f4;
    --orchid: #c7a6d9;
    --lily: #d9a3d6;
  }
  * { margin: 0; padding: 0; box-sizing: border-box; }
  html, body { width: 1200px; height: 1200px; overflow: hidden; background: var(--page); }
  .canvas { position: relative; width: 1200px; height: 1200px; }
  .label {
    position: absolute; left: 380px; top: 25px; width: 440px; height: 1150px;
    overflow: hidden; color: var(--white);
  }
  .label__wash {
    position: absolute; inset: 0;
    background:
      linear-gradient(160deg, var(--mint) 0%, var(--aqua) 10%, transparent 22%),
      linear-gradient(150deg, var(--teal) 0%, var(--ocean) 35%, var(--teal) 55%, var(--aqua) 75%, var(--teal) 100%);
  }
  .brand {
    position: absolute; top: 66px; left: 0; width: 100%; text-align: center;
    font-family: "Cormorant Garamond", serif; font-weight: 600; font-size: 42px;
    letter-spacing: 5px; text-transform: uppercase; white-space: nowrap;
  }
  .flower { position: absolute; }
  .flower--orchid {
    left: 0; top: 205px; width: 226px; height: 280px; border-radius: 40% 50% 45% 30%;
    background: radial-gradient(circle at 45% 45%, var(--white), var(--orchid-light) 45%, var(--orchid) 80%, transparent 100%);
  }
  .flower--lily-side {
    left: 300px; top: 584px; width: 140px; height: 364px; border-radius: 60% 0 0 50%;
    background: radial-gradient(circle at 90% 40%, var(--lily), var(--orchid-light) 60%, transparent 100%);
  }
  .flower--lily-low {
    left: 210px; top: 758px; width: 230px; height: 222px; border-radius: 50%;
    background: radial-gradient(circle at 50% 55%, var(--orchid-light), var(--lily) 55%, transparent 100%);
  }
  .scent-name {
    position: absolute; left: 93px; top: 453px; width: 252px; height: 253px;
    background: var(--deep); padding: 5px;
  }
  .scent-name__frame {
    width: 100%; height: 100%; border: 1.5px solid rgba(255,255,255,0.7);
    display: flex; flex-direction: column; justify-content: center; align-items: center;
    font-family: "Playfair Display", serif; font-weight: 400; font-size: 54px; line-height: 1.1;
    text-transform: uppercase;
  }
  .product-type {
    position: absolute; left: 95px; top: 990px; width: 252px; height: 95px;
    background: var(--deep); padding: 5px;
  }
  .product-type__frame {
    width: 100%; height: 100%; border: 1.5px solid rgba(255,255,255,0.7);
    display: flex; flex-direction: column; justify-content: center; align-items: center;
    font-family: "Cormorant Garamond", serif; text-transform: uppercase;
  }
  .product-type__small { font-size: 18px; letter-spacing: 4px; font-weight: 600; line-height: 1.1; }
  .product-type__main { font-size: 36px; font-weight: 500; line-height: 1.05; }
  .volume {
    position: absolute; left: 0; top: 1090px; width: 100%; text-align: center;
    font-family: "Cormorant Garamond", serif; font-size: 28px; font-weight: 500;
  }
</style>
</head>
<body>
<main class="canvas">
  <section class="label">
    <div class="label__wash" role="img" aria-label="Sweeping turquoise and ocean blue brushstroke background"></div>
    <div class="brand">Lunar Bramble</div>
    <div class="flower flower--orchid" role="img" aria-label="White and lilac orchid blossoms with dew drops"></div>
    <div class="flower flower--lily-side" role="img" aria-label="Pink lily blossom at the label edge"></div>
    <div class="flower flower--lily-low" role="img" aria-label="Pink lily blossom near the bottom"></div>
    <div class="scent-name"><div class="scent-name__frame"><span>Coral</span><span>Drift</span></div></div>
    <div class="product-type"><div class="product-type__frame">
      <span class="product-type__small">Fragance</span>
      <span class="product-type__main">Body Mist</span>
    </div></div>
    <div class="volume">℮ 250ml/8.4fl.oz</div>
  </section>
</main>
</body>
</html>
```